Create new graphics and layout for Quillmarsh Expansion Deck

Quillmarsh is a b2b fintech focused on identifying, refining, valuing, and monetizing data. It gives companies an opportunity to use their unused data and generate a revenue stream. We want to make pages that creatively communicate this. Additionally we want the graphics to elicit trust and brand recognition. The current capabilities deck provided does not achieve this goal so we encourage you to provide your best ideas, using the brand guidelines provided.

Please use a light or white background
Brand and Typesetting is provided in the Branding Guidelines document
Current draft is attached called Quillmarsh Expansion Plan Oct 17 - Final (Redacted) for Pixelbazaar pages 1-10
VIsuals should be engaging but not too distracting.
We are open to all other images and overall design, while maintaining the brand guidelines. Please be creative but again professional and demonstrate that Quillmarsh is a high tech, innovative and creative firm.
Subtle background images are also encouraged, as appropriate
Please do not grab images or graphics from the Quillmarsh website and we are redoing the website and do not like for most of the graphics on that website.
We are re-doing the copy so you can use placeholder text.

```html
<!DOCTYPE html>
<html lang="en">
<head>
<meta charset="utf-8">
<title>Quillmarsh Expansion Deck – Slide Overview</title>
<link href="https://fonts.googleapis.com/css2?family=Nunito:wght@800;900&family=Quicksand:wght@400;500;600;700&display=swap" rel="stylesheet">
<style>
:root{
  --teal:#2a8a8c;
  --teal-dark:#1f6f78;
  --green:#4db848;
  --blue:#3c9fe2;
  --navy:#1b4b7e;
  --ink:#3a4550;
  --muted:#8a949c;
  --line:#dde4e8;
  --paper:#ffffff;
  --mint:#e4f4ec;
  --sky:#e2eefa;
}
*{margin:0;padding:0;box-sizing:border-box}
html,body{width:1200px;height:986px;overflow:hidden;background:var(--paper)}
body{position:relative;font-family:"Quicksand",sans-serif;color:var(--ink)}
.slide{position:absolute;width:344px;height:190px;background:var(--paper);overflow:hidden;
  box-shadow:0 8px 14px rgba(40,60,70,.14)}
.slide>*{position:absolute}
.blob{border-radius:50%;filter:blur(6px);opacity:.75}
.blob.mint{background:radial-gradient(circle,#d4efdf 0%,rgba(228,244,236,0) 70%)}
.blob.sky{background:radial-gradient(circle,#cfe2f6 0%,rgba(226,238,250,0) 70%)}
.brand{top:9px;left:9px;display:flex;align-items:center;gap:3px;font-weight:700;font-size:7px;color:var(--navy)}
.brand i{width:11px;height:11px;border-radius:50%;border:1.6px solid var(--navy);display:block}
.pager{right:10px;bottom:8px;font-size:4px;color:var(--blue);display:flex;align-items:center;gap:3px}
.pager b{border-left:.8px solid var(--navy);padding-left:3px;color:var(--navy);font-weight:700}
.tag{font-size:4.2px;color:var(--green);display:flex;align-items:center;gap:3px;white-space:nowrap}
.tag::before{content:"";width:10px;height:.8px;background:var(--navy)}
.title{font-family:"Nunito",sans-serif;font-weight:900;color:var(--teal);font-size:14px;white-space:nowrap;line-height:1}
.body{font-size:3.8px;line-height:1.75;color:var(--ink)}
.card{background:#fff;border:.6px solid var(--line);box-shadow:0 2px 4px rgba(0,0,0,.08);
  clip-path:polygon(0 0,100% 0,100% 78%,84% 100%,0 100%)}
.photo{background:linear-gradient(135deg,#1f7c5a,#27a06c 55%,#0f4b3a)}
.bar-track{height:2.4px;background:#e6ebee;border-radius:2px}
.bar-fill{height:100%;border-radius:2px}
.small{font-size:4px}
.center{text-align:center}
</style>
</head>
<body>

<!-- 1 Cover -->
<section class="slide" style="left:47px;top:57px">
  <div class="blob sky" style="left:200px;top:20px;width:150px;height:150px"></div>
  <div class="blob mint" style="left:-30px;top:120px;width:120px;height:110px"></div>
  <div class="blob sky" style="left:280px;top:140px;width:40px;height:40px"></div>
  <div class="title" style="left:0;right:0;top:72px;text-align:center;font-size:29px">Quillmarsh</div>
  <div class="center" style="left:112px;top:111px;width:118px;height:14px;border:.6px solid var(--line);font-size:4.2px;color:var(--blue);line-height:13px;background:#fff">Welcome To New World of Digitalism</div>
</section>

<!-- 2 Introduction -->
<section class="slide" style="left:428px;top:57px">
  <div class="blob mint" style="left:40px;top:20px;width:80px;height:80px"></div>
  <div class="blob sky" style="left:250px;top:40px;width:110px;height:110px"></div>
  <div class="blob mint" style="left:-20px;top:140px;width:90px;height:80px"></div>
  <div class="brand"><i></i>Quillmarsh</div>
  <div class="tag" style="left:137px;top:33px">Quillmarsh Technology</div>
  <div class="title" style="left:0;right:0;top:43px;text-align:center">Introduction Quillmarsh</div>
  <div class="body center" style="left:60px;right:60px;top:77px">Lorem ipsum dolor sit amet, consectetuer adipiscing elit. Maecenas porttitor congue massa. Fusce posuere, magna sed pulvinar ultricies, purus lectus malesuada libero</div>
  <div class="card" style="left:29px;top:123px;width:53px;height:40px"></div>
  <div class="small" style="left:33px;top:151px">Lorem Ipsum</div>
  <div class="card" style="left:107px;top:123px;width:53px;height:40px;background:linear-gradient(135deg,var(--teal),var(--teal-dark));border:none"></div>
  <div class="small" style="left:111px;top:151px;color:#fff">Lorem Ipsum</div>
  <div class="card" style="left:186px;top:123px;width:53px;height:40px"></div>
  <div class="small" style="left:190px;top:151px">Lorem Ipsum</div>
  <div class="card" style="left:264px;top:123px;width:53px;height:40px"></div>
  <div class="small" style="left:268px;top:151px">Lorem Ipsum</div>
  <svg style="left:29px;top:123px" width="290" height="30" viewBox="0 0 290 30" fill="none" stroke-width=".8">
    <rect x="23" y="7" width="7" height="11" rx="3.5" stroke="var(--blue)"/>
    <path d="M95 11l8-4 8 4-8 4z M95 14l8 4 8-4" stroke="#fff"/>
    <path d="M175 10l-3 3 3 3 M185 10l3 3-3 3" stroke="var(--blue)"/>
    <rect x="254" y="7" width="6" height="9" stroke="var(--blue)"/><path d="M256 16v3h2v-3" stroke="var(--blue)"/>
  </svg>
  <div class="pager"><span>page</span><b>2</b></div>
</section>

<!-- 3 Experiences -->
<section class="slide" style="left:808px;top:57px">
  <div class="blob mint" style="left:120px;top:40px;width:90px;height:90px"></div>
  <div class="blob sky" style="left:-20px;top:130px;width:80px;height:80px"></div>
  <div class="brand"><i></i>Quillmarsh</div>
  <div class="tag" style="left:27px;top:42px">Quillmarsh Technology</div>
  <div class="title" style="left:23px;top:53px">Our Experiences</div>
  <div class="small" style="left:27px;top:104px;font-size:5px">January</div>
  <div class="small" style="left:127px;top:104px;font-size:5px">92%</div>
  <div class="bar-track" style="left:27px;top:113px;width:114px"><div class="bar-fill" style="width:92%;background:linear-gradient(90deg,var(--navy),var(--blue))"></div></div>
  <div class="small" style="left:27px;top:146px;font-size:5px">February</div>
  <div class="small" style="left:127px;top:146px;font-size:5px">70%</div>
  <div class="bar-track" style="left:27px;top:155px;width:114px"><div class="bar-fill" style="width:70%;background:linear-gradient(90deg,var(--teal),var(--green))"></div></div>

  <div style="left:157px;top:45px;width:22px;height:16px;background:var(--blue);clip-path:polygon(25% 0,100% 0,75% 100%,0 100%)"></div>
  <div class="card" style="left:172px;top:48px;width:144px;height:30px"></div>
  <div style="left:188px;top:52px;font-size:5.6px">Lorem Ipsum One</div>
  <div class="body" style="left:182px;top:61px;font-size:3.4px;width:120px">Lorem ipsum dolor sit amet, consectetuer adipiscing elit. Maecenas porttitor congue massa.</div>

  <div style="left:157px;top:86px;width:22px;height:16px;background:var(--green);clip-path:polygon(25% 0,100% 0,75% 100%,0 100%)"></div>
  <div class="card" style="left:172px;top:89px;width:144px;height:30px"></div>
  <div style="left:188px;top:93px;font-size:5.6px">Lorem Ipsum One</div>
  <div class="body" style="left:182px;top:102px;font-size:3.4px;width:120px">Lorem ipsum dolor sit amet, consectetuer adipiscing elit. Maecenas porttitor congue massa.</div>

  <div style="left:157px;top:127px;width:22px;height:16px;background:var(--teal);clip-path:polygon(25% 0,100% 0,75% 100%,0 100%)"></div>
  <div class="card" style="left:172px;top:130px;width:144px;height:30px"></div>
  <div style="left:188px;top:134px;font-size:5.6px">Lorem Ipsum One</div>
  <div class="body" style="left:182px;top:143px;font-size:3.4px;width:120px">Lorem ipsum dolor sit amet, consectetuer adipiscing elit. Maecenas porttitor congue massa.</div>
  <div class="pager"><span>page</span><b>3</b></div>
</section>

<!-- 4 Leader Team -->
<section class="slide" style="left:47px;top:284px">
  <div class="blob mint" style="left:270px;top:10px;width:100px;height:100px"></div>
  <div class="blob mint" style="left:250px;top:140px;width:90px;height:70px"></div>
  <div class="brand"><i></i>Quillmarsh</div>
  <div class="photo" role="img" aria-label="Portrait of the team leader against a green wall" style="left:31px;top:35px;width:92px;height:92px;clip-path:polygon(20% 0,100% 0,100% 80%,80% 100%,0 100%,0 20%)"></div>
  <div role="img" aria-label="Abstract teal smoke cloud" style="left:70px;top:72px;width:74px;height:92px;background:linear-gradient(160deg,#cfe6dc,#3c8a74 55%,#123f36);clip-path:polygon(30% 0,100% 0,100% 75%,70% 100%,0 100%,0 25%)"></div>
  <div class="card" style="left:124px;top:72px;width:60px;height:78px;background:linear-gradient(140deg,#e7eefc,#e8f6ee);clip-path:polygon(20% 0,100% 0,100% 70%,65% 100%,0 100%,0 20%)"></div>
  <div style="left:144px;top:117px;font-size:6px">Teo Marlow</div>
  <div style="left:141px;top:126px;font-size:4px;color:var(--muted)">Leader &nbsp;Team</div>
  <div class="tag" style="left:195px;top:42px">Quillmarsh Technology</div>
  <div class="title" style="left:192px;top:55px">Leader Team</div>
  <div style="left:203px;top:100px;font-family:Nunito,sans-serif;font-weight:900;color:var(--green);font-size:9px">“</div>
  <div class="body" style="left:210px;top:104px;width:98px;font-size:4.2px">Lorem ipsum dolor sit amet, consectetuer adipiscing elit. Maecenas porttitor congue massa. Fusce posuere, magna.</div>
  <div style="left:306px;top:122px;font-family:Nunito,sans-serif;font-weight:900;color:var(--green);font-size:9px">”</div>
  <div class="pager"><span>page</span><b>4</b></div>
</section>

<!-- 5 Expertise -->
<section class="slide" style="left:428px;top:284px">
  <div class="blob mint" style="left:270px;top:60px;width:100px;height:100px"></div>
  <div class="blob sky" style="left:100px;top:120px;width:60px;height:60px"></div>
  <div class="brand"><i></i>Quillmarsh</div>
  <div role="img" aria-label="Close-up of a hand wearing a smartwatch at a desk" style="left:31px;top:42px;width:114px;height:113px;background:linear-gradient(150deg,#3c3c3c,#1b1b1b 50%,#5b5148);clip-path:polygon(20% 0,100% 0,100% 80%,80% 100%,0 100%,0 20%)"></div>
  <div class="card" style="left:124px;top:87px;width:79px;height:48px"></div>
  <div style="left:124px;width:79px;top:93px;text-align:center;font-family:Nunito,sans-serif;font-weight:900;color:var(--teal);font-size:11px">2022</div>
  <div class="body" style="left:131px;top:109px;width:66px">Lorem ipsum dolor sit amet, consectetuer adipiscin.</div>
  <div class="card" style="left:53px;top:121px;width:37px;height:49px;background:linear-gradient(160deg,#e4eefb,#e6f5ec)"></div>
  <div style="left:53px;width:37px;top:139px;text-align:center;font-family:Nunito,sans-serif;font-weight:900;color:var(--teal);font-size:10px">$735</div>
  <div class="tag" style="left:195px;top:42px">Quillmarsh Technology</div>
  <div class="title" style="left:192px;top:55px">Our Expertise</div>
  <div class="body" style="left:225px;top:100px;width:90px">Lorem ipsum dolor sit amet, consectetuer adipiscing elit. Maecenas porttitor congue massa.</div>
  <div class="pager"><span>page</span><b>5</b></div>
</section>

<!-- 6 Percentage -->
<section class="slide" style="left:808px;top:284px">
  <div class="blob mint" style="left:-20px;top:110px;width:100px;height:100px"></div>
  <div class="blob mint" style="left:240px;top:20px;width:90px;height:80px"></div>
  <div class="brand"><i></i>Quillmarsh</div>
  <svg style="left:42px;top:48px" width="90" height="90" viewBox="0 0 90 90" fill="none">
    <circle cx="45" cy="45" r="41" stroke="var(--sky)" stroke-width="1"/>
    <circle cx="45" cy="45" r="41" stroke="var(--green)" stroke-width="1.6" stroke-dasharray="185 300" transform="rotate(-90 45 45)" pathLength="257"/>
    <circle cx="45" cy="45" r="41" stroke="var(--blue)" stroke-width="1.6" stroke-dasharray="0 120 70 300" transform="rotate(-90 45 45)" pathLength="257"/>
    <circle cx="74" cy="74" r="2" fill="var(--blue)"/>
  </svg>
  <div style="left:42px;width:90px;top:82px;text-align:center;font-family:Nunito,sans-serif;font-weight:900;color:var(--teal);font-size:19px">72%</div>
  <div class="card" style="left:29px;top:110px;width:40px;height:25px"></div>
  <div style="left:29px;width:40px;top:114px;text-align:center;font-size:3.8px">February</div>
  <div style="left:29px;width:40px;top:120px;text-align:center;font-size:5.4px;color:var(--blue)">+45%</div>
  <div class="tag" style="left:186px;top:48px">Quillmarsh Technology</div>
  <div class="title" style="left:182px;top:61px">Our Percentage</div>
  <svg style="left:185px;top:96px" width="100" height="8" viewBox="0 0 100 8" fill="none" stroke="var(--teal)" stroke-width=".6">
    <path d="M2 3l6-2.5 6 2.5-6 2.5z M2 5l6 2.5 6-2.5"/>
    <path d="M71 2h12l-1 4h-10z"/>
  </svg>
  <div class="body" style="left:185px;top:106px;width:58px;font-size:3.5px">Lorem ipsum dolor sit amet, consectetuer adipiscing elit. Maecenas porttitor.</div>
  <div class="body" style="left:255px;top:106px;width:58px;font-size:3.5px">Lorem ipsum dolor sit amet, consectetuer adipiscing elit. Maecenas porttitor.</div>
  <div class="pager"><span>page</span><b>6</b></div>
</section>

<!-- 7 Our Team -->
<section class="slide" style="left:47px;top:511px">
  <div class="blob mint" style="left:60px;top:0;width:90px;height:60px"></div>
  <div class="blob mint" style="left:20px;top:130px;width:80px;height:80px"></div>
  <div class="blob mint" style="left:250px;top:110px;width:100px;height:80px"></div>
  <div class="brand"><i></i>Quillmarsh</div>
  <div class="tag" style="left:131px;top:17px">Quillmarsh Technology</div>
  <div class="title" style="left:0;right:0;top:27px;text-align:center">Our Team</div>

  <div class="photo" role="img" aria-label="Team member portrait, green backdrop" style="left:20px;top:54px;width:66px;height:58px;clip-path:polygon(0 0,90% 0,100% 12%,100% 100%,12% 100%,0 88%)"></div>
  <div role="img" aria-label="Team member portrait, red backdrop" style="left:101px;top:54px;width:66px;height:58px;background:linear-gradient(135deg,#d12a36,#8e1520);clip-path:polygon(0 0,90% 0,100% 12%,100% 100%,12% 100%,0 88%)"></div>
  <div role="img" aria-label="Team member portrait, winter outdoors" style="left:181px;top:54px;width:66px;height:58px;background:linear-gradient(135deg,#dfe8f2,#5f87b2 60%,#2c4a73);clip-path:polygon(0 0,90% 0,100% 12%,100% 100%,12% 100%,0 88%)"></div>
  <div role="img" aria-label="Team member portrait, city street" style="left:262px;top:54px;width:66px;height:58px;background:linear-gradient(135deg,#e9eef4,#6aa8c8 55%,#2a3f63);clip-path:polygon(0 0,90% 0,100% 12%,100% 100%,12% 100%,0 88%)"></div>
  <div style="left:60px;top:87px;width:24px;height:24px;background:#10303b;border:.6px solid var(--green)"></div>
  <div style="left:141px;top:87px;width:24px;height:24px;background:#10303b;border:.6px solid var(--green)"></div>
  <div style="left:221px;top:87px;width:24px;height:24px;background:#10303b;border:.6px solid var(--green)"></div>
  <div style="left:302px;top:87px;width:24px;height:24px;background:#10303b;border:.6px solid var(--green)"></div>

  <div style="left:24px;top:124px;font-size:4.6px">Rian Okafor</div>
  <div class="body" style="left:24px;top:132px;width:60px;font-size:3.6px">Lorem ipsum dolor sit amet, consectetuer</div>
  <div style="left:105px;top:124px;font-size:4.6px">Rian Okafor</div>
  <div class="body" style="left:105px;top:132px;width:60px;font-size:3.6px">Lorem ipsum dolor sit amet, consectetuer</div>
  <div style="left:185px;top:124px;font-size:4.6px">Rian Okafor</div>
  <div class="body" style="left:185px;top:132px;width:60px;font-size:3.6px">Lorem ipsum dolor sit amet, consectetuer</div>
  <div style="left:266px;top:124px;font-size:4.6px">Rian Okafor</div>
  <div class="body" style="left:266px;top:132px;width:60px;font-size:3.6px">Lorem ipsum dolor sit amet, consectetuer</div>
  <div class="pager"><span>page</span><b>7</b></div>
</section>

<!-- 8 Bar chart -->
<section class="slide" style="left:428px;top:511px">
  <div class="blob mint" style="left:-20px;top:120px;width:90px;height:90px"></div>
  <div class="blob mint" style="left:250px;top:100px;width:110px;height:100px"></div>
  <div class="brand"><i></i>Quillmarsh</div>
  <div class="card" style="left:36px;top:40px;width:128px;height:128px;clip-path:none"></div>
  <div style="left:36px;width:128px;top:47px;text-align:center;font-size:4.2px">Lorem Ipsum for This Chart</div>
  <svg style="left:38px;top:56px" width="124" height="110" viewBox="0 0 124 110" font-family="Quicksand,sans-serif" font-size="3.2" fill="var(--blue)">
    <g text-anchor="end">
      <text x="20" y="10">$4,000.00</text><text x="20" y="21.5">$3,500.00</text><text x="20" y="33">$3,000.00</text>
      <text x="20" y="44.5">$2,500.00</text><text x="20" y="56">$2,000.00</text><text x="20" y="67.5">$1,500.00</text>
      <text x="20" y="79">$1,000.00</text><text x="20" y="90.5">$500.00</text><text x="20" y="102">$0.00</text>
    </g>
    <line x1="24" y1="101" x2="118" y2="101" stroke="var(--line)" stroke-width=".5"/>
    <defs>
      <linearGradient id="b1" x1="0" y1="0" x2="0" y2="1"><stop offset="0" stop-color="#2a7fd0"/><stop offset="1" stop-color="#0d2240"/></linearGradient>
      <linearGradient id="b2" x1="0" y1="0" x2="0" y2="1"><stop offset="0" stop-color="#4db848"/><stop offset="1" stop-color="#2b8fd8"/></linearGradient>
      <linearGradient id="b3" x1="0" y1="0" x2="0" y2="1"><stop offset="0" stop-color="#4db848"/><stop offset="1" stop-color="#3aa84a"/></linearGradient>
    </defs>
    <rect x="32" y="73" width="10" height="28" fill="url(#b1)"/>
    <rect x="61" y="48" width="10" height="53" fill="url(#b2)"/>
    <rect x="90" y="36" width="10" height="65" fill="url(#b3)"/>
    <text x="37" y="108" text-anchor="middle">2018</text><text x="66" y="108" text-anchor="middle">2019</text><text x="95" y="108" text-anchor="middle">2020</text>
  </svg>
  <div class="card" style="left:107px;top:69px;width:28px;height:22px"></div>
  <div style="left:107px;width:28px;top:77px;text-align:center;font-size:4.6px">13%</div>
  <div class="tag" style="left:195px;top:45px">Quillmarsh Technology</div>
  <div class="title" style="left:192px;top:55px">Our Chart</div>
  <div class="body" style="left:194px;top:80px;width:96px">Lorem ipsum dolor sit amet, consectetuer adipiscing elit.</div>
  <div class="card" style="left:197px;top:115px;width:90px;height:48px"></div>
  <div style="left:233px;top:125px;font-size:6px">2019 - 2020</div>
  <div style="left:248px;top:137px;font-family:Nunito,sans-serif;font-weight:900;color:var(--teal);font-size:10px">13%</div>
  <svg style="left:206px;top:132px" width="20" height="18" viewBox="0 0 20 18" fill="var(--teal)">
    <path d="M1 1v16h18" stroke="var(--navy)" stroke-width=".6" fill="none"/>
    <circle cx="5" cy="13" r=".8"/><circle cx="8" cy="10" r=".8"/><circle cx="11" cy="11" r=".8"/><circle cx="13" cy="7" r=".8"/><circle cx="16" cy="5" r=".8"/><circle cx="17" cy="9" r=".8"/>
  </svg>
  <div class="pager"><span>page</span><b>8</b></div>
</section>

<!-- 9 Donut chart -->
<section class="slide" style="left:808px;top:511px">
  <div class="blob mint" style="left:-10px;top:110px;width:90px;height:90px"></div>
  <div class="brand"><i></i>Quillmarsh</div>
  <div class="tag" style="left:34px;top:45px">Quillmarsh Technology</div>
  <div class="title" style="left:31px;top:55px">Our Chart</div>
  <div style="left:27px;top:100px;width:57px;height:31px;background:linear-gradient(135deg,var(--blue),var(--navy));clip-path:polygon(0 0,80% 0,100% 25%,100% 100%,0 100%)"></div>
  <div class="card" style="left:43px;top:93px;width:20px;height:12px;clip-path:none"></div>
  <div style="left:43px;width:20px;top:95px;text-align:center;font-size:4px;font-weight:700;color:var(--blue)">Feb</div>
  <div style="left:37px;top:112px;width:44px;font-size:3.5px;line-height:1.6;color:#fff">Lorem ipsum dolor sit amet consectetur</div>
  <div style="left:95px;top:123px;width:58px;height:30px;background:linear-gradient(135deg,var(--teal),var(--green));clip-path:polygon(0 0,80% 0,100% 25%,100% 100%,0 100%)"></div>
  <div class="card" style="left:111px;top:116px;width:22px;height:12px;clip-path:none"></div>
  <div style="left:111px;width:22px;top:118px;text-align:center;font-size:4px;font-weight:700;color:var(--green)">Marc</div>
  <div style="left:105px;top:134px;width:44px;font-size:3.5px;line-height:1.6;color:#fff">Lorem ipsum dolor sit amet consectetur</div>
  <svg style="left:205px;top:50px" width="100" height="96" viewBox="0 0 100 96" fill="none">
    <circle cx="50" cy="48" r="41" stroke="var(--navy)" stroke-width="10" stroke-dasharray="0 120 137 0" pathLength="257" transform="rotate(-90 50 48)"/>
    <circle cx="50" cy="48" r="41" stroke="var(--blue)" stroke-width="10" stroke-dasharray="0 40 80 200" pathLength="257" transform="rotate(-90 50 48)"/>
    <circle cx="50" cy="48" r="41" stroke="var(--green)" stroke-width="10" stroke-dasharray="40 300" pathLength="257" transform="rotate(-90 50 48)"/>
    <circle cx="50" cy="48" r="41" stroke="#7cc0ee" stroke-width="10" stroke-dasharray="0 257 0" pathLength="257"/>
  </svg>
  <div class="card" style="left:200px;top:88px;width:24px;height:14px;clip-path:none"></div>
  <div style="left:200px;width:24px;top:90px;text-align:center;font-size:3px">February</div>
  <div style="left:200px;width:24px;top:95px;text-align:center;font-size:3.6px;color:var(--green)">3,000</div>
  <div class="card" style="left:282px;top:66px;width:24px;height:14px;clip-path:none"></div>
  <div style="left:282px;width:24px;top:68px;text-align:center;font-size:3px">March</div>
  <div style="left:282px;width:24px;top:73px;text-align:center;font-size:3.6px">2,000</div>
  <div style="left:226px;top:147px;font-size:3.6px;display:flex;gap:14px">
    <span><span style="display:inline-block;width:2.5px;height:2.5px;background:var(--navy)"></span> Data One</span>
    <span><span style="display:inline-block;width:2.5px;height:2.5px;background:var(--blue)"></span> Data Two</span>
  </div>
  <div class="pager"><span>page</span><b>9</b></div>
</section>

<!-- 10 Process chart -->
<section class="slide" style="left:47px;top:738px">
  <div class="blob mint" style="left:-10px;top:120px;width:90px;height:90px"></div>
  <div class="brand"><i></i>Quillmarsh</div>
  <div class="tag" style="left:131px;top:24px">Quillmarsh Technology</div>
  <div class="title" style="left:0;right:0;top:35px;text-align:center">Our Chart</div>
  <svg style="left:16px;top:70px" width="312" height="80" viewBox="0 0 312 80" fill="none" stroke-width=".6">
    <line x1="2" y1="39" x2="310" y2="39" stroke="var(--line)"/>
    <circle cx="2" cy="39" r="1.4" stroke="var(--line)" fill="#fff"/><circle cx="310" cy="39" r="1.4" stroke="var(--line)" fill="#fff"/>
    <g stroke="var(--muted)" stroke-dasharray="1 1">
      <path d="M82 14v15 M179 14v15 M276 14v15"/>
      <path d="M34 49v15 M131 49v15 M228 49v15"/>
    </g>
  </svg>
  <div style="left:33px;top:101px;width:34px;height:17px;background:linear-gradient(135deg,#5ab0ee,var(--blue))"></div>
  <div style="left:81px;top:101px;width:34px;height:17px;background:linear-gradient(135deg,var(--green),#35a04a)"></div>
  <div style="left:130px;top:101px;width:34px;height:17px;background:linear-gradient(135deg,var(--teal),var(--green))"></div>
  <div style="left:178px;top:101px;width:34px;height:17px;background:linear-gradient(135deg,var(--blue),var(--navy))"></div>
  <div style="left:227px;top:101px;width:34px;height:17px;background:linear-gradient(135deg,#5ab0ee,var(--blue))"></div>
  <div style="left:275px;top:101px;width:34px;height:17px;background:linear-gradient(135deg,var(--green),var(--blue))"></div>
  <div style="left:178px;width:34px;top:104px;text-align:center;font-size:4.6px;line-height:1;color:#fff">1010<br>1010</div>

  <div class="center small" style="left:68px;width:60px;top:74px">Lorem Ipsum Two</div>
  <div class="center" style="left:68px;width:60px;top:80px;font-size:3.2px;color:var(--muted)">Mr. Halden</div>
  <div class="center small" style="left:165px;width:60px;top:74px">Lorem Ipsum Four</div>
  <div class="center" style="left:165px;width:60px;top:80px;font-size:3.2px;color:var(--muted)">Mr. Orsi</div>
  <div class="center small" style="left:262px;width:60px;top:74px">Lorem Ipsum Six</div>
  <div class="center" style="left:262px;width:60px;top:80px;font-size:3.2px;color:var(--muted)">Mrs. Vell</div>
  <div class="center small" style="left:20px;width:60px;top:135px">Lorem Ipsum One</div>
  <div class="center" style="left:20px;width:60px;top:141px;font-size:3.2px;color:var(--muted)">Mr. Tam Pryce</div>
  <div class="center small" style="left:117px;width:60px;top:135px">Lorem Ipsum Three</div>
  <div class="center" style="left:117px;width:60px;top:141px;font-size:3.2px;color:var(--muted)">Van Holt</div>
  <div class="center small" style="left:214px;width:60px;top:135px">Lorem Ipsum Five</div>
  <div class="center" style="left:214px;width:60px;top:141px;font-size:3.2px;color:var(--muted)">Mrs. Ilse</div>
  <div class="pager"><span>page</span><b>10</b></div>
</section>

<!-- 11 Contact -->
<section class="slide" style="left:428px;top:738px">
  <div class="blob mint" style="left:-10px;top:120px;width:90px;height:90px"></div>
  <div class="brand"><i></i>Quillmarsh</div>
  <div class="tag" style="left:32px;top:48px">Quillmarsh Technology</div>
  <div class="title" style="left:31px;top:59px">Contact Us</div>
  <div style="left:31px;top:79px;font-size:5px;color:var(--green)">Customer Service Agents are Available 24/7.</div>
  <div style="left:32px;top:114px;font-size:4.4px;color:var(--blue)">Our Address</div>
  <div class="body" style="left:32px;top:122px;width:56px;font-size:3.5px">Quillmarsh – Road No. 4 Professional Services</div>
  <div class="card" style="left:93px;top:107px;width:76px;height:42px"></div>
  <div style="left:103px;top:114px;font-size:4.4px;color:var(--blue)">Contact Us</div>
  <svg style="left:106px;top:123px" width="8" height="16" viewBox="0 0 8 16" fill="none" stroke="var(--blue)" stroke-width=".5">
    <path d="M1.5 1.5l2 0 .8 2-1 .8a4 4 0 0 0 1.5 1.5l.8-1 2 .8v2c-3 .5-6.5-3-6.1-6.1z"/>
    <rect x="1" y="11" width="6" height="4"/><path d="M1 11l3 2 3-2"/>
  </svg>
  <div style="left:117px;top:124px;font-size:3.6px">555-014-2290</div>
  <div style="left:117px;top:134px;font-size:3.6px">hello@quillmarsh.co</div>
  <div style="left:229px;top:56px;width:12px;height:12px;background:var(--teal)"></div>
  <div style="left:257px;top:59px;font-size:4.2px">news.quillmarsh.co</div>
  <div style="left:229px;top:83px;width:12px;height:12px;background:var(--blue)"></div>
  <div style="left:257px;top:86px;font-size:4.2px">gallery.quillmarsh.co</div>
  <div style="left:229px;top:110px;width:12px;height:12px;background:var(--teal)"></div>
  <div style="left:257px;top:113px;font-size:4.2px">updates.quillmarsh.co</div>
  <div style="left:229px;top:137px;width:12px;height:12px;background:var(--blue)"></div>
  <div style="left:257px;top:140px;font-size:4.2px">careers.quillmarsh.co</div>
  <div class="pager"><span>page</span><b>11</b></div>
</section>

<!-- 12 Thank you -->
<section class="slide" style="left:808px;top:738px">
  <div class="blob mint" style="left:-10px;top:120px;width:90px;height:90px"></div>
  <div class="blob sky" style="left:250px;top:10px;width:90px;height:80px"></div>
  <div class="title" style="left:0;right:0;top:57px;text-align:center;font-size:27px">Thank You</div>
  <div style="left:98px;top:90px;width:148px;height:1px;background:linear-gradient(90deg,var(--navy),var(--green))"></div>
  <div class="body center" style="left:90px;right:90px;top:97px;font-size:3.6px">Lorem ipsum dolor sit amet, consectetuer adipiscing elit. Maecen portion congue massa. Fusce posuere, magna sed pulvinar ultricies, purus lectus.</div>
  <div style="left:137px;top:126px;width:10px;height:10px;border-radius:50%;border:.7px solid var(--blue)"></div>
  <div style="left:164px;top:126px;width:10px;height:10px;border-radius:50%;border:.7px solid var(--blue)"></div>
  <div style="left:191px;top:126px;width:10px;height:10px;border-radius:50%;border:.7px solid var(--green)"></div>
</section>

</body>
</html>
```